Halvern Properties Business Cards

I would like a business card that includes myself and my partner.
Includes: Logo, office #, email, website, our names, our numbers and possibly the address. I would also like the logo to be embossed and the card to be horizontal.
There is a photo of our yard signs to give you an idea of the colors of our business.

Target Market(s)

Everyone in real estate market.
We are in a rural area. Our clientele are from all socioeconomic backgrounds.

Industry/Entity Type

Real Estate Agent

Contact Information for Business Card

Company Name: Halvern Properties
Our Names, Titles & Cell #'s : Marla Halvern-Broker (555).316.4827, Tessa Halvern-Realtor (555).627.9154
Office #: (555).841.2600
Website: halvernproperties-example.com
Joint Email: halvern@halvernproperties-example.com
Office Address: 518B W. Cottonwell Ave.
Brazoria, TX. 70999

Font styles to use
Serif

Requirements
Must have
• HORIZONTAL, Logo, Myself and my partners names, Our cell #'s, our office #, our website, our email address
Nice to have
• Embossed logo, office address, our titles.

```html
<!DOCTYPE html>
<html lang="en">
<head>
<meta charset="utf-8">
<title>Halvern Properties Business Cards</title>
<link href="https://fonts.googleapis.com/css2?family=Cormorant+Garamond:wght@600&family=Arimo:wght@400;700&display=swap" rel="stylesheet">
<style>
  :root {
    --purple: #7a4aa8;
    --purple-deep: #5e2f8e;
    --ink: #0d0d0d;
    --paper: #f7f7f7;
    --backdrop: #e4e2df;
    --muted: #d8d8d8;
  }
  html, body { margin: 0; padding: 0; overflow: hidden; }
  body {
    width: 1200px; height: 902px;
    background: var(--backdrop);
    position: relative;
    font-family: "Arimo", Arial, sans-serif;
  }
  .card {
    position: absolute;
    left: 250px;
    width: 700px; height: 400px;
    background: var(--paper);
    box-shadow: 0 6px 18px rgba(0,0,0,.18);
    overflow: hidden;
  }
  .card--front { top: 28px; }
  .card--back { top: 474px; }

  .wordmark {
    font-family: "Cormorant Garamond", Georgia, serif;
    font-weight: 600;
    color: var(--purple);
    text-align: center;
    line-height: 1;
    position: absolute;
  }
  .wordmark__line1 { display: block; font-size: 64px; letter-spacing: 2px; }
  .wordmark__line2 { display: block; font-size: 40px; margin-top: 6px; }
  .card--front .wordmark { left: 0; right: 0; top: 130px; }
  .card--back .wordmark { left: 170px; top: 40px; }
  .card--back .wordmark__line1 { font-size: 56px; }
  .card--back .wordmark__line2 { font-size: 34px; }

  .wave { position: absolute; inset: 0; }

  .agents {
    position: absolute;
    left: 24px; bottom: 26px;
    display: flex;
    color: #fff;
  }
  .agent { padding: 0 12px; text-align: right; }
  .agent + .agent { border-left: 1.5px solid #fff; }
  .agent__name { font-weight: 700; font-size: 20px; white-space: nowrap; }
  .agent__title { font-size: 16px; color: var(--muted); }
  .agent__cell { font-size: 12px; color: var(--muted); margin-top: 3px; white-space: nowrap; }

  .contacts {
    position: absolute;
    left: 404px; top: 222px;
    padding-left: 18px;
    border-left: 1.5px solid #fff;
    height: 150px;
    display: flex; flex-direction: column; justify-content: space-between;
    color: #fff;
    font-size: 12px;
    white-space: nowrap;
  }
  .contact { display: flex; align-items: center; gap: 9px; }
  .contact--address { font-size: 11px; }
  .contact svg { width: 16px; height: 16px; flex: none; }
</style>
</head>
<body>

<section class="card card--front" aria-label="Card front">
  <div class="wordmark">
    <span class="wordmark__line1">HALVERN</span>
    <span class="wordmark__line2">Properties</span>
  </div>
</section>

<section class="card card--back" aria-label="Card back">
  <svg class="wave" viewBox="0 0 700 400" width="700" height="400" aria-hidden="true">
    <path d="M0,272 C150,282 260,282 360,212 C450,152 560,112 700,112 L700,400 L0,400 Z" fill="var(--purple)"/>
    <path d="M0,290 C150,300 260,300 360,230 C450,170 560,130 700,130 L700,400 L0,400 Z" fill="#ffffff"/>
    <path d="M0,294 C150,304 260,304 360,234 C450,174 560,134 700,134 L700,400 L0,400 Z" fill="var(--ink)"/>
  </svg>

  <div class="wordmark">
    <span class="wordmark__line1">HALVERN</span>
    <span class="wordmark__line2">Properties</span>
  </div>

  <div class="agents">
    <div class="agent">
      <div class="agent__name">Tessa Halvern</div>
      <div class="agent__title">Realtor</div>
      <div class="agent__cell">(555).627.9154</div>
    </div>
    <div class="agent">
      <div class="agent__name">Marla Halvern</div>
      <div class="agent__title">Broker</div>
      <div class="agent__cell">(555).316.4827</div>
    </div>
  </div>

  <div class="contacts">
    <div class="contact">
      <svg viewBox="0 0 16 16"><circle cx="8" cy="8" r="7.5" fill="#fff"/><rect x="4" y="5" width="8" height="6" fill="none" stroke="#000" stroke-width="1.2"/><path d="M4,5 L8,8.5 L12,5" fill="none" stroke="#000" stroke-width="1.2"/></svg>
      <span>halvern@halvernproperties-example.com</span>
    </div>
    <div class="contact">
      <svg viewBox="0 0 16 16"><rect x="4" y="1" width="8" height="14" rx="1.5" fill="#fff"/><rect x="5.5" y="3" width="5" height="7" fill="#000"/></svg>
      <span>Office (555).841.2600</span>
    </div>
    <div class="contact">
      <svg viewBox="0 0 16 16"><circle cx="8" cy="8" r="7" fill="none" stroke="#fff" stroke-width="1.4"/><ellipse cx="8" cy="8" rx="3" ry="7" fill="none" stroke="#fff" stroke-width="1.2"/><path d="M1,8 H15" stroke="#fff" stroke-width="1.2"/></svg>
      <span>halvernproperties-example.com</span>
    </div>
    <div class="contact contact--address">
      <svg viewBox="0 0 16 16"><path d="M1,8 L8,2 L15,8" fill="none" stroke="#fff" stroke-width="1.6"/><path d="M3.5,7.5 V14 H12.5 V7.5" fill="#fff"/><rect x="7" y="10" width="2" height="4" fill="#000"/></svg>
      <span>518B W. Cottonwell Ave. Brazoria, TX. 70999</span>
    </div>
  </div>
</section>

</body>
</html>
```